Clara Joy Halden- Lantern Waltz- Autumn/Winter Tour Dates

I need high res A3 Tour poster for print and for social media JPG sharing of tour dates.
Also needed Facebook/Twitter Banner Cover Photos of these dates.
Text Needed Below
Clara Joy Halden
Lantern Waltz
Autumn/Winter Tour Dates
03/09 Ravensby Folk Festival
21/09 Swindon- Calder Theatre
01/10 Hitchin- Brackwell Folk Club
17/10 Bath- The Anvil
20/10 Sheffield- Upper Dale Croquet Club
24/10 Birmingham- Orchard Lamp Cafe
26/10 Glasgow- The Nook and Jar
27/10 Edinburgh - The Marble Parlour
08/11 Capital Reel and Ballad Festival- The Crooked Heron
25/11 Lewes- Tandem Record Shop- Live In Store
02/12 Cambridge- The Quayside
27/01 Lincolnshire- Fenmarsh Theatre
Tickets/Info: www.clarajoyhalden-music.example/gigs
(Quotes/Reviews To Put On)
"Outstanding, rich and expressive."            "Vibrant and Experimental"
**** BdM                                                               **** Tunepaths
"Impressive and Invigorating"                        "Enchanting" Acoustic Wire UK
tBarks

Updates
I cannot read the tour dates on most of the submissions so far. They need to be visible to viewers.
Thank You.
Please also be as creative and inventive as possible- not bland.

Target Market(s)
Music Fans- Folk Acoustic Americana
Industry/Entity Type
Media
Font styles to use
Requirements
Must have
- My photo featured prominently
- Look classy and not tacky or OTT
- Look elegant, wintery and eye catching
- The dates must be very clear to read
- Links to Website:

Nice to have
- Something innovative and not boring in terms of layout design
- Perhaps fading/ misty or wintery

Should not have
- Any colours that do not match

```html
<!DOCTYPE html>
<html lang="en">
<head>
<meta charset="utf-8">
<title>Clara Joy Halden – Lantern Waltz Tour Dates</title>
<link rel="stylesheet" href="https://fonts.googleapis.com/css2?family=Parisienne&family=Tinos:wght@400;700&display=swap">
<style>
  :root {
    --night: #07080d;
    --night-mid: #151a28;
    --mist: #2a3245;
    --hair: #1a2030;
    --glow: #b9c0d6;
    --glow-soft: #6f7891;
    --frost: #b3bdea;
    --frost-deep: #6b7cc0;
    --date-blue: #8d9dd6;
    --snow: #ffffff;
    --rule: #3b4770;
    --icon: #4c6bb3;
  }
  * { margin: 0; padding: 0; box-sizing: border-box; }
  html, body { width: 849px; height: 1200px; overflow: hidden; background: var(--night); }
  .poster { position: relative; width: 849px; height: 1200px; overflow: hidden; font-family: "Tinos", "Times New Roman", serif; color: var(--snow);
    background: radial-gradient(ellipse 520px 420px at 720px 260px, var(--night-mid) 0%, rgba(7,8,13,0) 100%), var(--night); }
  .portrait-photo {
    position: absolute; left: 400px; top: 360px; width: 449px; height: 840px;
    background:
      radial-gradient(ellipse 105px 140px at 235px 255px, var(--glow) 0%, rgba(150,158,182,0.65) 45%, rgba(80,90,115,0) 100%),
      radial-gradient(ellipse 70px 120px at 225px 520px, rgba(185,192,214,0.55) 0%, rgba(80,90,115,0) 100%),
      radial-gradient(ellipse 230px 330px at 240px 330px, var(--mist) 0%, var(--hair) 55%, rgba(20,24,36,0) 100%),
      radial-gradient(ellipse 260px 300px at 260px 120px, rgba(111,120,145,0.55) 0%, rgba(40,46,64,0) 100%),
      linear-gradient(180deg, rgba(21,26,40,0) 0%, #10141f 60%, var(--night) 100%);
    -webkit-mask-image: linear-gradient(90deg, transparent 0%, #000 30%);
    mask-image: linear-gradient(90deg, transparent 0%, #000 30%);
  }
  .artist-name { position: absolute; top: 72px; left: 0; width: 849px; text-align: center; font-family: "Parisienne", cursive; font-size: 64px; line-height: 1; }
  .tour-title { position: absolute; left: 66px; top: 150px; font-family: "Tinos", "Times New Roman", serif; font-weight: 400; font-size: 120px; line-height: 122px; letter-spacing: 1px;
    color: var(--frost); text-shadow: 3px 3px 0 #000; }
  .season { position: absolute; left: 78px; top: 468px; font-size: 23px; font-weight: 700; letter-spacing: 0.3px; }
  .dates-heading { position: absolute; left: 78px; top: 496px; font-size: 42px; font-weight: 700; letter-spacing: 0.5px; color: var(--date-blue); }
  .rule { position: absolute; left: 78px; width: 348px; height: 1px; background: var(--rule); }
  .rule--heading { top: 566px; background: var(--date-blue); }
  .rule--heading::after { content: ""; position: absolute; left: 168px; top: -3px; width: 7px; height: 7px; border-radius: 50%; background: var(--date-blue); }
  .rule--quotes { top: 968px; }
  .rule--footer { top: 1117px; }
  .gig-list { position: absolute; left: 78px; top: 592px; list-style: none; font-size: 18px; line-height: 28px; font-weight: 700; }
  .gig { display: flex; }
  .gig--wrap { line-height: 22px; padding: 3px 0; }
  .gig-date { width: 71px; color: var(--date-blue); }
  .reviews { position: absolute; left: 78px; top: 988px; font-size: 17px; line-height: 22px; }
  .reviews p + p.gap { margin-top: 14px; }
  .stars { font-size: 11px; letter-spacing: 1px; vertical-align: 2px; }
  .source { color: var(--date-blue); }
  .tickets { position: absolute; left: 78px; top: 1138px; font-size: 19px; font-weight: 700; color: var(--date-blue); }
  .social { position: absolute; left: 566px; top: 1102px; list-style: none; font-size: 18px; font-family: "Tinos", "Times New Roman", serif; }
  .social li { display: flex; align-items: center; height: 26px; margin-bottom: 12px; }
  .social-dot { width: 25px; height: 25px; border-radius: 50%; background: var(--icon); margin-right: 10px; }
</style>
</head>
<body>
<main class="poster">
  <div class="portrait-photo" role="img" aria-label="Photo of the singer in a crystal wire crown with long dark hair, against a dark misty winter backdrop"></div>

  <h1 class="artist-name">Clara Joy Halden</h1>
  <h2 class="tour-title">LANTERN<br>WALTZ</h2>

  <p class="season">AUTUMN/WINTER</p>
  <h3 class="dates-heading">TOUR DATES</h3>
  <div class="rule rule--heading"></div>

  <ul class="gig-list">
    <li class="gig"><span class="gig-date">03/09</span><span class="gig-venue">Ravensby Folk Festival</span></li>
    <li class="gig"><span class="gig-date">21/09</span><span class="gig-venue">Swindon- Calder Theatre</span></li>
    <li class="gig"><span class="gig-date">01/10</span><span class="gig-venue">Hitchin- Brackwell Folk Club</span></li>
    <li class="gig"><span class="gig-date">17/10</span><span class="gig-venue">Bath- The Anvil</span></li>
    <li class="gig"><span class="gig-date">20/10</span><span class="gig-venue">Sheffield- Upper Dale Croquet Club</span></li>
    <li class="gig"><span class="gig-date">24/10</span><span class="gig-venue">Birmingham- Orchard Lamp Cafe</span></li>
    <li class="gig"><span class="gig-date">26/10</span><span class="gig-venue">Glasgow- The Nook and Jar</span></li>
    <li class="gig"><span class="gig-date">27/10</span><span class="gig-venue">Edinburgh - The Marble Parlour</span></li>
    <li class="gig gig--wrap"><span class="gig-date">08/11</span><span class="gig-venue">Capital Reel and Ballad Festival-<br>&nbsp;The Crooked Heron</span></li>
    <li class="gig"><span class="gig-date">25/11</span><span class="gig-venue">Lewes- Tandem Record Shop- Live In Store</span></li>
    <li class="gig"><span class="gig-date">02/12</span><span class="gig-venue">Cambridge- The Quayside</span></li>
    <li class="gig"><span class="gig-date">27/01</span><span class="gig-venue">Lincolnshire- Fenmarsh Theatre</span></li>
  </ul>

  <div class="rule rule--quotes"></div>
  <div class="reviews">
    <p>“Outstanding, rich and expressive.”<span class="stars">★★★★</span><span class="source">BdM</span></p>
    <p>“Vibrant and Experimental” <span class="stars">★★★★</span> <span class="source">Tunepaths</span></p>
    <p class="gap">“Impressive and Invigorating” <span class="source">Acoustic Wire UK</span></p>
    <p>“Enchanting” <span class="source">tBarks</span></p>
  </div>
  <div class="rule rule--footer"></div>

  <p class="tickets">Tickets/Info: www.clarajoyhalden-music.example/gigs</p>

  <ul class="social">
    <li><span class="social-dot"></span>@clarajoyhalden</li>
    <li><span class="social-dot"></span>clarajoyhaldenmusic</li>
  </ul>
</main>
</body>
</html>
```